Online Grocery Shopping Business Needs a Brochure

We are an e-commerce company that specialise in selling FRESH groceries and deliver them to our customer. The fresh groceries we offer include vegetables, fruits, seafood, meat (beef, pork, chicken) and yong tau foo, a chinese product where beancurds, peppers and various items are stuffed with fish and meat paste. We also offer other groceries such as cooking essentials like rice, household items such as washing detergents, and beverages like zuma-fizz. In order to retain the freshness of our products, we handpick the items from the suppliers daily, pack them in a cold and insulated environment, and deliver it to our customers on the very same day.

We know it’s not easy waking up early in the morning and carrying all the heavy bags of groceries home. Therefore, we want to do it for our customers, so they can do what’s really important to them like spending time with their loved ones.

We are looking for creative and innovative 4-paged front and back A5 brochure designs that will highlight the freshness of our products and also the convenience we bring to customers. The brochure should include the following information:

1. The 8 categories of product
i. Fresh Vegetables
ii. Fresh Fruits
iii. Fresh Seafood
iv. Fresh Meat
v. Yong Tau Foo
vii. Cooking Essentials
viii. Beverages

2. Packing/Delivery Process
i. Handpicking fresh products from supplier
ii. Packed into a low temperature and insulated environment
iii. Delivering the same day

3. Delivery information
i. 10am – 10pm
ii. Tuesday to Sundays (including Public Holidays)
iii. 2 hour delivery slots
a. 10am – 12pm
b. 12pm – 2pm
c. 2pm – 4pm
d. 4pm – 6pm
e. 6 pm – 8pm
f. 8pm – 10pm
iv. Next day delivery (except Monday)

4. Web URL: www.crispbasket.com.sg

5. Contact/Social Media
i. Email: enquiries@crispbasket.com.sg
ii. Phone: 8174 6052
iii. Facebook

6. Announce Promotion: Key in Coupon Code for discount

Attached is our logo design. Kindly visit our website at www.crispbasket.com.sg for reference.

Target Market(s)

Working Adults, Housewives, Families,

Industry/Entity Type

Environment

Requirements
Must have
• Showcase FRESHNESS of our groceries and the CONVENIENT service we offer.
Nice to have
• Direct viewer's attention to key points for each page. Such as taking customers for a visual "walkthrough" of our product categories.
Should not have
• Prices of items.

```html
<!DOCTYPE html>
<html lang="en">
<head>
<meta charset="utf-8">
<title>Crisp Basket – Product Categories Spread</title>
<link href="https://fonts.googleapis.com/css2?family=Oswald:wght@500;600&family=Open+Sans:wght@400&display=swap" rel="stylesheet">
<style>
  :root {
    --backdrop: #e6e6e6;
    --paper: #ffffff;
    --brand-green: #3d9a1f;
    --ink: #1e1e1e;
    --caption-box: rgba(255, 255, 255, 0.74);
  }
  * { box-sizing: border-box; margin: 0; padding: 0; }
  html, body { width: 1200px; height: 800px; overflow: hidden; }
  body { background: var(--backdrop); position: relative; }

  .spread {
    position: absolute; left: 63px; top: 20px;
    width: 1074px; height: 760px;
    display: flex;
    box-shadow: 0 6px 24px rgba(0,0,0,.18);
  }
  .page {
    width: 537px; height: 760px; background: var(--paper);
    display: grid;
    grid-template-rows: 46px repeat(4, 1fr) 50px;
    row-gap: 10px;
  }
  .page--left { padding: 0 4px 0 16px; }
  .page--right { padding: 0 16px 0 4px; }

  .page-tagline, .page-footer {
    font-family: "Oswald", sans-serif; font-weight: 600;
    color: var(--brand-green); text-transform: uppercase;
    display: flex; align-items: center; justify-content: center;
    letter-spacing: .2px;
  }
  .page-tagline { font-size: 17px; align-self: end; }
  .page-footer { font-size: 17px; align-self: start; padding-top: 6px; }
  .page-footer .url { color: var(--brand-green); }

  .category {
    position: relative; overflow: hidden;
  }
  .category-photo { position: absolute; inset: 0; }
  .category-caption {
    position: absolute; top: 8px; bottom: 8px;
    background: var(--caption-box);
    padding: 8px 12px;
    color: var(--ink);
  }
  .category-title {
    font-family: "Oswald", sans-serif; font-weight: 500;
    font-size: 23px; line-height: 1.05; text-transform: uppercase;
    margin-bottom: 3px;
  }
  .category-list {
    list-style: none;
    font-family: "Open Sans", sans-serif; font-size: 10.5px; line-height: 1.17;
  }

  .photo-vegetables { background: linear-gradient(90deg, #b8241b 0%, #d7cdbf 22%, #8a5a32 45%, #6d4527 100%); }
  .photo-fruit { background: linear-gradient(90deg, #f08a1c 0%, #e9b33c 25%, #c8243a 55%, #f2f0e6 75%, #e8791a 100%); }
  .photo-meat { background: linear-gradient(90deg, #6c2a26 0%, #b8706a 35%, #d9b3ab 65%, #c9812e 85%, #8f3b30 100%); }
  .photo-seafood { background: linear-gradient(90deg, #3f6f8f 0%, #9a6f7a 30%, #c9cdd2 55%, #e07a4a 80%, #b9c4cc 100%); }
  .photo-essentials { background: linear-gradient(90deg, #4a7a2a 0%, #e3e3e0 25%, #8a2f2a 45%, #e8dcc2 75%, #6b4a2a 100%); }
  .photo-yongtaufoo { background: linear-gradient(90deg, #8e7a6a 0%, #e8e2d8 30%, #c98b8e 55%, #f1c4c6 80%, #d99aa0 100%); }
  .photo-beverages { background: linear-gradient(90deg, #f2f2f2 0%, #c7d5e2 20%, #e2a23c 45%, #f4f4f4 65%, #7fb4d6 80%, #e28a2c 100%); }
  .photo-household { background: linear-gradient(90deg, #cfe7a8 0%, #eef6e2 40%, #9ccf6a 70%, #e46a4a 85%, #7fbf4a 100%); }
</style>
</head>
<body>
<main class="spread">

  <section class="page page--left">
    <h1 class="page-tagline">Crisp Basket - The Freshest Groceries Directly At Your Doorstep!</h1>

    <article class="category">
      <div class="category-photo photo-vegetables" role="img" aria-label="Fresh vegetables: red peppers, garlic, chillies and lettuce on a wooden board"></div>
      <div class="category-caption" style="left:246px; width:208px;">
        <h2 class="category-title">Vegetables</h2>
        <ul class="category-list">
          <li>Leafy Greens</li>
          <li>Radish, Potato &amp; Root Vegetables</li>
          <li>Pumpkin, Melon &amp; Squash</li>
          <li>Mushrooms, Beans &amp; Corn</li>
          <li>Lettuce, Cabbage &amp; Salad</li>
          <li>Chilli, Herbs &amp; Spices</li>
          <li>Ginger, Garlic &amp; Onion</li>
        </ul>
      </div>
    </article>

    <article class="category">
      <div class="category-photo photo-fruit" role="img" aria-label="Fresh fruit: oranges, strawberries, apples and pineapple"></div>
      <div class="category-caption" style="left:46px; width:202px;">
        <h2 class="category-title">Fruit</h2>
        <ul class="category-list">
          <li>Apples &amp; Pears</li>
          <li>Berries, Cherries &amp; Grapes</li>
          <li>Exotic &amp; Tropical Fruits</li>
          <li>Melons, Pineapple &amp; Papaya</li>
          <li>Oranges &amp; Citrus</li>
        </ul>
      </div>
    </article>

    <article class="category">
      <div class="category-photo photo-meat" role="img" aria-label="Fresh raw meat cuts, sausages and herbs"></div>
      <div class="category-caption" style="left:246px; width:206px;">
        <h2 class="category-title">Fresh Meat</h2>
        <ul class="category-list">
          <li>Pork</li>
          <li>Beef</li>
          <li>Mutton</li>
          <li>Duck</li>
          <li>Chicken</li>
          <li>Eggs</li>
        </ul>
      </div>
    </article>

    <article class="category">
      <div class="category-photo photo-seafood" role="img" aria-label="Fresh seafood: octopus, prawns and fish on ice"></div>
      <div class="category-caption" style="left:46px; width:208px;">
        <h2 class="category-title">Fresh Seafood</h2>
        <ul class="category-list">
          <li>Whole Fish</li>
          <li>Sliced Fish</li>
          <li>Prawns, Crab &amp; Cockles</li>
          <li>Stingray, Squid &amp; Sea Cucumber</li>
          <li>Scallops &amp; Abalone</li>
        </ul>
      </div>
    </article>

    <p class="page-footer">Order today at&nbsp;<span class="url">www.crispbasket.com.sg</span></p>
  </section>

  <section class="page page--right">
    <div aria-hidden="true"></div>

    <article class="category">
      <div class="category-photo photo-essentials" role="img" aria-label="Cooking essentials: salt, peppercorns, basil, garlic and oil"></div>
      <div class="category-caption" style="left:222px; width:190px;">
        <h2 class="category-title">Cooking Essentials</h2>
        <ul class="category-list">
          <li>Condiments &amp; Dressing</li>
          <li>Oil</li>
          <li>Sugar, Salt &amp; Pepper</li>
          <li>Flour &amp; Starch</li>
          <li>Rice &amp; Pasta</li>
          <li>Dried Products</li>
        </ul>
      </div>
    </article>

    <article class="category">
      <div class="category-photo photo-yongtaufoo" role="img" aria-label="Yong tau foo ingredients: fish paste, tofu and dumplings"></div>
      <div class="category-caption" style="left:36px; width:222px;">
        <h2 class="category-title">Yong Tau Foo</h2>
        <ul class="category-list">
          <li>Ingredients with Fish Paste</li>
          <li>Beancurd &amp; Tofu</li>
          <li>Fishball &amp; Fishcake</li>
          <li>Meatballs, Hotdogs &amp; Chilled Varieties</li>
          <li>Noodles &amp; Mee</li>
          <li>Wanton, Dumpling &amp; Ngo Hiang</li>
        </ul>
      </div>
    </article>

    <article class="category">
      <div class="category-photo photo-beverages" role="img" aria-label="Assorted bottled and canned drinks"></div>
      <div class="category-caption" style="left:222px; width:190px;">
        <h2 class="category-title">Beverages</h2>
        <ul class="category-list">
          <li>Zuma-Fizz &amp; Kola Bay</li>
          <li>Leaf &amp; Stone</li>
          <li>Zippa &amp; Sunny Press</li>
          <li>Orvio &amp; Fizzeta</li>
          <li>Sports &amp; Energy</li>
          <li>Limora, Clearfizz &amp; Ridge Rush</li>
          <li>Lin's &amp; Teatime</li>
        </ul>
      </div>
    </article>

    <article class="category">
      <div class="category-photo photo-household" role="img" aria-label="Household cleaning supplies in a basket"></div>
      <div class="category-caption" style="left:36px; width:200px;">
        <h2 class="category-title">Household</h2>
        <ul class="category-list">
          <li>Tissue &amp; Toilet Paper</li>
          <li>Laundry Washing</li>
          <li>Dishwashing</li>
          <li>Toothpaste</li>
        </ul>
      </div>
    </article>

    <p class="page-footer">Turn the page for a special discount coupon code &gt;&gt;&gt;</p>
  </section>

</main>
</body>
</html>
```